Bref créative
Business Stationary Package for a Business & Personal Consulting Firm
Beyond Ledger Lines
I need double sided standard sized Business Card [3.5" x 2"]
Something that goes great with the logo
Bright & Fun-filled
Varun Mehta
Registered Tax Return Preparer
20417 Brisbury Ln
Charlotte, NC 28105-4419
varun@beyondledgerlines.example
www.beyondledgerlines.example
At the conclusion of this project, I am expecting editable design files of business cards, letterheads, fax coversheet, email-signature, and a folder.
Note 1: I would be interested in design of business cards, folder, etc with a colored background.
Note 2: I would like to see the designs of letterheads with the watermark of logo.
I would like to see the logo and web address on the back side along with list of services (Incorporation, Bookkeeping & Accounting, Taxation, personal budgeting). As mentioned above I would be curious to see how a colored background would look.

```html
<!DOCTYPE html>
<html lang="en">
<head>
<meta charset="utf-8">
<title>Beyond Ledger Lines — Stationery Set</title>
<link rel="stylesheet" href="https://fonts.googleapis.com/css2?family=Montserrat:wght@400;600;700&display=swap">
<style>
  :root {
    --red: #c8202f;
    --charcoal: #3a3a3c;
    --charcoal-dark: #2f2f31;
    --halo: #47474a;
    --paper: #ffffff;
    --backdrop: #e9e9e9;
    --ink: #4a4a4a;
    --muted: #9a9a9a;
    --rule: #d6d6d6;
    --watermark: #f3f3f3;
  }
  * { box-sizing: border-box; margin: 0; padding: 0; }
  html, body { width: 1200px; height: 504px; overflow: hidden; }
  body {
    background: var(--backdrop);
    font-family: "Montserrat", sans-serif;
    color: var(--ink);
    position: relative;
  }
  .piece { position: absolute; overflow: hidden; box-shadow: 0 1px 3px rgba(0,0,0,.12); }

  /* Brand lockup */
  .brand { display: flex; align-items: center; gap: 4px; white-space: nowrap; }
  .brand-dot { border-radius: 50%; background: var(--red); flex: none; }
  .brand-name { font-weight: 700; text-transform: uppercase; letter-spacing: .05em; line-height: 1; }
  .tagline { font-size: 4.4px; letter-spacing: .14em; text-transform: uppercase; color: var(--muted); white-space: nowrap; }

  /* Letterhead */
  .letterhead { left: 173px; top: 29px; width: 211px; height: 295px; background: var(--paper); }
  .letterhead .watermark { position: absolute; left: 48px; top: 100px; width: 130px; height: 130px; border-radius: 50%; background: var(--watermark); }
  .letterhead .head { position: absolute; top: 14px; left: 0; right: 0; display: flex; flex-direction: column; align-items: center; gap: 3px; }
  .letterhead .brand-name { font-size: 9px; color: var(--red); }
  .letterhead .brand-dot { width: 7px; height: 7px; }
  .letterhead .body { position: absolute; left: 20px; right: 30px; top: 50px; font-size: 3.6px; line-height: 5.6px; color: #777; }
  .letterhead .body p { margin-bottom: 4px; }
  .letterhead .signature { margin-top: 10px; font-weight: 600; color: var(--ink); }
  .footer-line { position: absolute; left: 0; right: 0; bottom: 20px; height: 2px; background: var(--charcoal); }
  .footer-band { position: absolute; left: 0; right: 0; bottom: 0; height: 16px; background: var(--red); color: #fff; font-size: 3.6px; display: flex; align-items: center; justify-content: center; gap: 10px; letter-spacing: .04em; white-space: nowrap; }

  /* Folder */
  .folder { left: 420px; top: 24px; width: 480px; height: 300px; background: var(--charcoal); }
  .folder .fold { position: absolute; left: 240px; top: 0; bottom: 0; width: 1px; background: var(--charcoal-dark); }
  .folder .halo { position: absolute; left: 262px; top: 60px; width: 200px; height: 200px; border-radius: 50%; background: var(--halo); }
  .folder .mark { position: absolute; left: 80px; top: 108px; width: 80px; height: 80px; border-radius: 50%; background: var(--red); }
  .folder .accent { position: absolute; height: 1.5px; background: var(--red); }
  .folder .lockup { position: absolute; left: 290px; top: 122px; display: flex; flex-direction: column; gap: 3px; }
  .folder .brand-name { font-size: 17px; color: #fff; letter-spacing: .1em; }
  .folder .lockup .tagline { color: #bdbdbd; font-size: 4.6px; margin-top: 3px; }
  .folder .band { position: absolute; left: 0; right: 0; bottom: 16px; height: 12px; display: flex; }
  .folder .band-half { flex: 1; display: flex; align-items: center; justify-content: center; border-top: 1px solid var(--red); border-bottom: 1px solid var(--red); }
  .folder .band-half span { font-size: 4.4px; color: #fff; letter-spacing: .24em; text-transform: uppercase; font-weight: 600; white-space: nowrap; }

  /* Fax cover */
  .fax { left: 955px; top: 29px; width: 212px; height: 295px; background: var(--paper); }
  .fax .watermark { position: absolute; left: 58px; top: 80px; width: 110px; height: 110px; border-radius: 50%; background: var(--watermark); }
  .fax .head { position: absolute; top: 14px; left: 0; right: 0; display: flex; flex-direction: column; align-items: center; gap: 3px; }
  .fax .brand-name { font-size: 9px; color: var(--red); }
  .fax .brand-dot { width: 7px; height: 7px; }
  .fax .title { position: absolute; right: 20px; top: 46px; font-size: 7px; font-weight: 600; color: var(--ink); }
  .fax .fields { position: absolute; left: 14px; right: 14px; top: 62px; display: grid; grid-template-columns: repeat(4, 1fr); gap: 6px 6px; }
  .fax .field { display: flex; align-items: center; gap: 3px; font-size: 3.6px; color: var(--ink); border-bottom: 1px solid var(--rule); padding-bottom: 2px; white-space: nowrap; }
  .fax .field i { width: 4px; height: 4px; background: var(--charcoal); display: block; flex: none; }

  /* Business cards */
  .card { width: 101px; height: 46px; background: var(--charcoal); color: #fff; }
  .card .brand { position: absolute; left: 8px; top: 9px; }
  .card .brand-name { font-size: 6px; color: #fff; }
  .card .brand-dot { width: 5px; height: 5px; }
  .card .stripe { position: absolute; left: 0; right: 0; bottom: 0; height: 7px; background: var(--red); font-size: 3.2px; display: flex; align-items: center; justify-content: center; letter-spacing: .08em; white-space: nowrap; }
  .card .lines { position: absolute; left: 8px; top: 19px; font-size: 3.2px; line-height: 4.4px; color: #d0d0d0; white-space: nowrap; }
  .card .lines strong { font-size: 3.8px; color: #fff; font-weight: 600; }

  /* Envelopes */
  .envelope { left: 221px; top: 360px; width: 228px; height: 120px; background: var(--paper); }
  .envelope .brand { position: absolute; left: 10px; top: 10px; }
  .envelope .brand-name { font-size: 6px; color: var(--red); }
  .envelope .brand-dot { width: 5px; height: 5px; }
  .envelope .return { position: absolute; left: 10px; top: 20px; font-size: 3.4px; line-height: 4.6px; color: var(--muted); }
  .envelope-back { left: 470px; top: 360px; width: 231px; height: 120px; background: var(--paper); }
  .envelope-back svg { position: absolute; inset: 0; }
</style>
</head>
<body>

  <section class="piece letterhead">
    <div class="watermark"></div>
    <header class="head">
      <div class="brand"><span class="brand-dot"></span><span class="brand-name">Beyond Ledger Lines</span></div>
      <div class="tagline">Business &amp; Personal Consulting</div>
    </header>
    <div class="body">
      <p>Dear Client,</p>
      <p>Thank you for choosing our team. We review your records, prepare returns and plan budgets with care.</p>
      <p>Please find the enclosed summary for your review.</p>
      <p>Kind regards,</p>
      <p class="signature">Varun Mehta</p>
    </div>
    <div class="footer-line"></div>
    <footer class="footer-band">
      <span>20417 Brisbury Ln, Charlotte, NC 28105-4419</span>
      <span>www.beyondledgerlines.example</span>
    </footer>
  </section>

  <section class="piece folder">
    <div class="halo"></div>
    <div class="fold"></div>
    <div class="mark"></div>
    <div class="accent" style="left:280px; top:112px; width:200px;"></div>
    <div class="accent" style="left:250px; top:178px; width:230px;"></div>
    <div class="lockup">
      <span class="brand-name">Beyond Ledger</span>
      <span class="brand-name">Lines</span>
      <span class="tagline">Business &amp; Personal Consulting</span>
    </div>
    <div class="band">
      <div class="band-half"><span>www.beyondledgerlines.example</span></div>
      <div class="band-half"><span>www.beyondledgerlines.example</span></div>
    </div>
  </section>

  <section class="piece fax">
    <div class="watermark"></div>
    <header class="head">
      <div class="brand"><span class="brand-dot"></span><span class="brand-name">Beyond Ledger Lines</span></div>
      <div class="tagline">Business &amp; Personal Consulting</div>
    </header>
    <div class="title">Fax</div>
    <div class="fields">
      <div class="field"><i></i>To</div>
      <div class="field"><i></i>From</div>
      <div class="field"><i></i>Fax</div>
      <div class="field"><i></i>Phone</div>
      <div class="field"><i></i>Date</div>
      <div class="field"><i></i>Pages</div>
      <div class="field"><i></i>Re</div>
      <div class="field"><i></i>CC</div>
    </div>
    <footer class="footer-band"><span>www.beyondledgerlines.example</span></footer>
  </section>

  <article class="piece card" style="left:96px; top:353px;">
    <div class="brand"><span class="brand-dot"></span><span class="brand-name">Beyond Ledger Lines</span></div>
    <div class="lines"><strong>Varun Mehta</strong><br>Registered Tax Return Preparer</div>
    <div class="stripe"></div>
  </article>
  <article class="piece card" style="left:96px; top:420px;">
    <div class="brand"><span class="brand-dot"></span><span class="brand-name">Beyond Ledger Lines</span></div>
    <div class="lines">20417 Brisbury Ln<br>Charlotte, NC 28105-4419</div>
    <div class="stripe"></div>
  </article>

  <section class="piece envelope">
    <div class="brand"><span class="brand-dot"></span><span class="brand-name">Beyond Ledger Lines</span></div>
    <div class="return">20417 Brisbury Ln<br>Charlotte, NC 28105-4419</div>
  </section>

  <section class="piece envelope-back">
    <svg width="231" height="120" viewBox="0 0 231 120">
      <polygon points="0,0 231,0 115.5,62" fill="var(--charcoal)"/>
      <polyline points="0,120 115.5,58 231,120" fill="none" stroke="var(--rule)" stroke-width="1"/>
    </svg>
  </section>

  <article class="piece card" style="left:734px; top:346px;">
    <div class="brand"><span class="brand-dot"></span><span class="brand-name">Beyond Ledger Lines</span></div>
    <div class="lines">Incorporation · Bookkeeping &amp; Accounting<br>Taxation · Personal Budgeting</div>
    <div class="stripe">www.beyondledgerlines.example</div>
  </article>
  <article class="piece card" style="left:734px; top:413px;">
    <div class="brand"><span class="brand-dot"></span><span class="brand-name">Beyond Ledger Lines</span></div>
    <div class="lines">varun@beyondledgerlines.example</div>
    <div class="stripe">www.beyondledgerlines.example</div>
  </article>

</body>
</html>
```